Update shopping site

Our current shopping website is outdated and we are wanting to update our shopping site to have a fresh new look/design.

Create a Web Design (Uncoded - PSD layout only)

We want you to develop the design for 4 pages:
1) Home Page
2) Remedy Type
3) Health Condition
4) Consultations

www.fernmoorwell.com

Reason: Close to choosing design and a few missing items to be resolved.

Industry/Entity Type

Shopping

```html
<!DOCTYPE html>
<html lang="en">
<head>
<meta charset="utf-8">
<title>Fernmoor Well — Why Choose Us</title>
<link rel="stylesheet" href="https://fonts.googleapis.com/css2?family=Josefin+Sans:wght@300;400;600&display=swap">
<style>
  :root {
    --forest: #035c3f;
    --mint: #8cc79a;
    --ink: #0d2219;
    --ink-soft: #12301f;
    --white: #ffffff;
    --photo-top: #7d9886;
    --photo-top-light: #a3b6a8;
    --photo-bottom: #6f9677;
  }
  * { box-sizing: border-box; margin: 0; padding: 0; }
  html, body { width: 936px; height: 1200px; overflow: hidden; }
  body { font-family: "Josefin Sans", sans-serif; background: var(--forest); position: relative; }

  .intro {
    position: absolute; left: 0; top: 0; width: 936px; height: 332px;
    background: linear-gradient(180deg, var(--photo-top) 0%, var(--photo-top-light) 70%, #b4c2b7 100%);
  }
  .intro-text {
    position: absolute; left: 78px; top: 2px; width: 780px;
    color: var(--white); text-align: center; text-transform: uppercase;
    font-weight: 400; font-size: 16px; letter-spacing: 3.9px; line-height: 32.8px;
  }

  .section-head { position: absolute; left: 0; width: 936px; text-align: center; }
  .section-title {
    color: var(--white); font-weight: 300; font-size: 37px; letter-spacing: 8px;
  }
  .section-sub {
    position: relative; margin: 8px auto 0; width: 544px;
    font-size: 17.5px; letter-spacing: 3.5px; font-weight: 400; color: var(--mint);
  }
  .section-sub::before, .section-sub::after {
    content: ""; position: absolute; top: 45%; width: 181px; height: 1px; background: var(--ink);
  }
  .section-sub::before { left: 0; }
  .section-sub::after { right: 0; }

  .services { top: 448px; }

  .service {
    position: absolute; width: 180px; text-align: center;
  }
  .service-icon {
    display: block; margin: 0 auto; width: 44px; height: 44px; border-radius: 8px; background: var(--ink);
  }
  .service-name {
    height: 26px; margin-top: 15px; display: flex; align-items: flex-start; justify-content: center;
    font-size: 9.6px; font-weight: 600; color: var(--ink); line-height: 11px;
  }
  .service-desc {
    font-size: 11.5px; font-weight: 300; color: var(--ink-soft); line-height: 15.5px;
  }
  .service-link {
    display: block; margin-top: 5px; font-size: 9.4px; color: var(--ink); text-decoration: none; letter-spacing: 0.3px;
  }

  .testimonials {
    position: absolute; left: 0; top: 1079px; width: 936px; height: 121px;
    background: linear-gradient(180deg, var(--photo-bottom), #7fa185);
  }
  .testimonials .section-head { top: 20px; }
  .testimonials .section-sub { color: #9fd1a2; opacity: .7; }
  .quote-mark {
    position: absolute; left: 0; top: 100px; width: 936px; text-align: center;
    color: var(--white); font-size: 60px; font-weight: 300; line-height: 1;
  }
</style>
</head>
<body>

<section class="intro" role="img" aria-label="Glass apothecary bottles holding fresh herb sprigs">
  <p class="intro-text">In our industry (we require certificate of analysis from our suppliers to ensure the purity of our product, that it is free of pesticides, contaminants, mold, fungus and it is the right product); we have over 300 NPN (Natural Product Number) licenses approved by the Herbal Standards Council and our friendly staff is well qualified to answer most questions you may have.&nbsp; We also partner with professional practitioners if you require a more thorough consultation</p>
</section>

<header class="section-head services">
  <h2 class="section-title">WHY CHOOSE US ?</h2>
  <p class="section-sub">OUR SERVICES</p>
</header>

<article class="service" style="left:70px;top:600px">
  <span class="service-icon" role="img" aria-label="Herb sprig icon"></span>
  <h3 class="service-name">Over 280 Organic<br>or Wild Crafted Herbs</h3>
  <p class="service-desc">Lorem ipsum dolor sit<br>amet, consectetur adipiscing elit.<br>Quisque ut...</p>
  <a class="service-link" href="#">LEARN MORE</a>
</article>
<article class="service" style="left:276px;top:600px">
  <span class="service-icon" role="img" aria-label="Tincture bottle icon"></span>
  <h3 class="service-name">Over 200 Single Tinctures</h3>
  <p class="service-desc">Lorem ipsum dolor sit<br>amet, consectetur adipiscing elit.<br>Quisque ut...</p>
  <a class="service-link" href="#">LEARN MORE</a>
</article>
<article class="service" style="left:480px;top:600px">
  <span class="service-icon" role="img" aria-label="Tea bag icon"></span>
  <h3 class="service-name">Medicinal Teas</h3>
  <p class="service-desc">Lorem ipsum dolor sit<br>amet, consectetur adipiscing elit.<br>Quisque ut...</p>
  <a class="service-link" href="#">LEARN MORE</a>
</article>
<article class="service" style="left:684px;top:600px">
  <span class="service-icon" role="img" aria-label="Cream jar icon"></span>
  <h3 class="service-name">Healing Creams and Salves</h3>
  <p class="service-desc">Lorem ipsum dolor sit<br>amet, consectetur adipiscing elit.<br>Quisque ut...</p>
  <a class="service-link" href="#">LEARN MORE</a>
</article>

<article class="service" style="left:70px;top:815px">
  <span class="service-icon" role="img" aria-label="Flower icon"></span>
  <h3 class="service-name">Wildbloom Flower Remedies</h3>
  <p class="service-desc">Lorem ipsum dolor sit<br>amet, consectetur adipiscing elit.<br>Quisque ut...</p>
  <a class="service-link" href="#">LEARN MORE</a>
</article>
<article class="service" style="left:276px;top:815px">
  <span class="service-icon" role="img" aria-label="Aroma bowl icon"></span>
  <h3 class="service-name">Aromatherapy</h3>
  <p class="service-desc">Lorem ipsum dolor sit<br>amet, consectetur adipiscing elit.<br>Quisque ut...</p>
  <a class="service-link" href="#">LEARN MORE</a>
</article>
<article class="service" style="left:480px;top:815px">
  <span class="service-icon" role="img" aria-label="Mortar and pestle icon"></span>
  <h3 class="service-name">Custom formulations</h3>
  <p class="service-desc">Lorem ipsum dolor sit<br>amet, consectetur adipiscing elit.<br>Quisque ut...</p>
  <a class="service-link" href="#">LEARN MORE</a>
</article>
<article class="service" style="left:684px;top:816px">
  <span class="service-icon" role="img" aria-label="Hand with oil drops icon"></span>
  <h3 class="service-name">Practitioner grade Essential Oils</h3>
  <p class="service-desc">Lorem ipsum dolor sit<br>amet, consectetur adipiscing elit.<br>Quisque ut...</p>
  <a class="service-link" href="#">LEARN MORE</a>
</article>

<section class="testimonials" role="img" aria-label="Soft-focus photo of a client consultation">
  <header class="section-head">
    <h2 class="section-title">WHAT CLIENTS SAY?</h2>
    <p class="section-sub">TESTIMONIALS</p>
  </header>
  <div class="quote-mark">&ldquo;</div>
</section>

</body>
</html>
```